Tri fold flyer design for restoration company

Use our website for inspiration and make a world class advertising tri fold flyer.
brookvalerestoration.com

Colors
0054AA
0677BA
7BADD7
CADEEF
E8F1F8
00AB8E
00BBA5
67D7C9
C6EFE9
E9F9F6
EB3D1F
EC4F4E
F09395
F8D3D4
FCEDEE

```html
<!DOCTYPE html>
<html lang="en">
<head>
<meta charset="utf-8">
<title>Brookvale Restoration – Services</title>
<link rel="stylesheet" href="https://fonts.googleapis.com/css2?family=Anton&family=Oswald:wght@300&family=Archivo:ital,wght@0,400;1,400&family=Montserrat:wght@700&display=swap">
<style>
  :root {
    --red: #d4432a;
    --navy: #1b3c8e;
    --ink: #111111;
    --white: #ffffff;
    --panel-blue: #b7d3df;
    --photo-warm: #ece4e0;
  }
  * { margin: 0; padding: 0; box-sizing: border-box; }
  html, body { width: 1200px; height: 848px; overflow: hidden; background: var(--white); }
  .flyer { position: relative; width: 1200px; height: 848px; overflow: hidden; background: var(--white); }

  .photo { position: absolute; }
  .photo--bedroom { left: 0; top: 0; width: 524px; height: 219px;
    background: linear-gradient(100deg, #ede6e2 0%, #f4f0ee 45%, #ebe7e6 100%); }
  .photo--sprayer { left: 418px; top: 19px; width: 176px; height: 245px;
    background: linear-gradient(160deg, #d8c8c2 0%, #ece9e8 50%, #cfc9c6 100%); }
  .photo--wiping { left: 604px; top: 114px; width: 176px; height: 176px;
    background: linear-gradient(135deg, #e9ecef 0%, #3e3c3c 55%, #6d8fbf 85%, #c69a63 100%); }

  .title { position: absolute; font-family: "Anton", sans-serif; color: var(--red);
    font-size: 41px; line-height: 41px; letter-spacing: 0.5px; text-transform: uppercase; }
  .title .thin { font-family: "Oswald", sans-serif; font-weight: 300; }
  .title .rule { display: inline-block; width: 110px; height: 4px; background: var(--red);
    vertical-align: middle; margin-left: 12px; }
  .title--left { left: 55px; top: 157px; }
  .title--right { left: 846px; top: 157px; }

  .service { position: absolute; width: 330px; }
  .service h2 { font-family: "Anton", sans-serif; font-weight: 400; color: var(--red);
    font-size: 20px; line-height: 24px; letter-spacing: 0.3px; display: flex; align-items: flex-end; gap: 12px; }
  .service h2 svg { flex: none; }
  .service p { font-family: "Archivo", sans-serif; color: var(--navy); font-size: 12.6px;
    line-height: 15.4px; margin-top: 7px; }
  .service p + p { margin-top: 15.4px; }

  .service--water { left: 55px; top: 312px; }
  .service--fire { left: 55px; top: 568px; }
  .service--mold { left: 445px; top: 310px; }
  .service--weather { left: 443px; top: 558px; }

  .panel { position: absolute; left: 798px; top: 0; width: 402px; height: 848px;
    background: linear-gradient(180deg, #bcd7e3 0%, #aecbd8 50%, #b5d1dd 100%); }
  .panel-intro { position: absolute; left: 846px; top: 313px; width: 340px;
    font-family: "Archivo", sans-serif; color: var(--red); font-size: 17px; line-height: 24.3px; }
  .extras { position: absolute; left: 847px; top: 500px; list-style: none; }
  .extras li { display: flex; align-items: center; gap: 12px; height: 37.7px;
    font-family: "Montserrat", sans-serif; font-weight: 700; color: var(--red); font-size: 15px; letter-spacing: 0.3px; }

  .foot-bar { position: absolute; left: 0; bottom: 0; width: 798px; height: 13px; background: var(--red); }
</style>
</head>
<body>
<main class="flyer">
  <div class="photo photo--bedroom" role="img" aria-label="Woman stretching happily on a bright white bed, softly faded"></div>
  <div class="photo photo--sprayer" role="img" aria-label="Technician in protective suit spraying disinfectant near an air conditioner"></div>
  <div class="photo photo--wiping" role="img" aria-label="Gloved hand wiping a surface with a blue cloth and spray mist"></div>

  <h1 class="title title--left">Residential <span class="thin">&amp;</span><br>Commercial<br><span class="thin">Services</span><span class="rule"></span></h1>

  <section class="service service--water">
    <h2>Water Damage
      <svg width="36" height="36" viewBox="0 0 36 36" aria-hidden="true"><path d="M18 2 L4 13 H8 V24 H28 V13 H32 Z" fill="var(--ink)"/><rect x="15" y="14" width="6" height="10" fill="#fff"/><circle cx="18" cy="9" r="2" fill="#fff"/><path d="M1 27 q4 -3 8 0 t8 0 t8 0 t8 0 M1 33 q4 -3 8 0 t8 0 t8 0 t8 0" stroke="var(--ink)" stroke-width="2.5" fill="none"/></svg>
    </h2>
    <p>Water damage is quite common among other disasters. A little amount of water in your home can create a huge loss and damage. This happens when we neglect this little amount and it becomes big within short span of time. The damange that can be repaired immediately takes few thousand dollars. This can damage antique furniture, wooden floors, expensive carpets, electric appliances, and lot more.</p>
    <p>Water also leads to form mold and becomes a great threat. Moisture in any part of area gives the ground for mold formation, bacteria and many insects. This needs immediate care by our experts before it becomes huge.</p>
  </section>

  <section class="service service--fire">
    <h2>Fire and Smoke Damage
      <svg width="28" height="38" viewBox="0 0 28 38" aria-hidden="true"><path d="M15 1 C17 10 27 14 26 25 C25 33 19 37 14 37 C7 37 2 32 2 25 C2 18 7 15 9 9 C10 14 12 16 14 17 C15 11 16 6 15 1 Z M14 35 C18 35 20 31 19 27 C18 24 16 22 15 19 C13 23 9 26 9 30 C9 33 11 35 14 35 Z" fill="var(--ink)" fill-rule="evenodd"/></svg>
    </h2>
    <p>Fire incidents are very common and can happen anytime. This experience is very frustrating for home owners and they are not sure what to do in such a disaster. This has to be handled very carefully by experts as many materials, equipments etc can blast, emit toxic gases, make construction weak and many things they are unaware.</p>
    <p>At <em>Brookvale</em>, we have team of experts that is ready to handle and manage such situations and provide professional service to get back in shape.</p>
  </section>

  <section class="service service--mold">
    <h2>Mold Damage
      <svg width="40" height="40" viewBox="0 0 40 40" aria-hidden="true"><g fill="var(--ink)"><circle cx="20" cy="20" r="12"/><g stroke="var(--ink)" stroke-width="3"><line x1="20" y1="2" x2="20" y2="38"/><line x1="2" y1="20" x2="38" y2="20"/><line x1="7" y1="7" x2="33" y2="33"/><line x1="33" y1="7" x2="7" y2="33"/></g><circle cx="20" cy="3" r="3"/><circle cx="20" cy="37" r="3"/><circle cx="3" cy="20" r="3"/><circle cx="37" cy="20" r="3"/><circle cx="7" cy="7" r="3"/><circle cx="33" cy="33" r="3"/><circle cx="33" cy="7" r="3"/><circle cx="7" cy="33" r="3"/></g><circle cx="16" cy="17" r="2.5" fill="#fff"/><circle cx="23" cy="23" r="2" fill="#fff"/></svg>
    </h2>
    <p>The development of Mold comes with moisture, excessive water, flooding, and many type of water leakages. This mold growth is huge threat to the belongings when it grows. It should be handled at first sight as it grows at fast rate and change the appearance of things. It should be stopped from growing or spreading any further.</p>
    <p>If the mold is left unchecked, it could further result in reduced indoor air quality and an unsafe environment. Molds can also attack paper, cardboard, and organic adhesives, as well as wallpaper and particle board.</p>
  </section>

  <section class="service service--weather">
    <h2>Weather Damage
      <svg width="44" height="36" viewBox="0 0 44 36" aria-hidden="true"><g stroke="var(--ink)" stroke-width="2.6" fill="none" stroke-linecap="round"><path d="M2 12 H24 A5 5 0 1 0 19 7"/><path d="M2 18 H36 A5 5 0 1 0 31 13"/><path d="M2 24 H26 A5 5 0 1 1 21 29"/></g></svg>
    </h2>
    <p>We are not sure of natural calamities that can happen anywhere, anytime. It can be anything like storm, lightning, earthquake that creates a huge loss and damage to properties. These are the situations that are very frustrating as we don't have the idea or experience to handle them. These needs to be handled by experts and professional teams so the things can be normal and back in shape as early as possible.</p>
    <p>We are professional and experts in handling these situations and help homeowners to get their property back in shape as efficiently as possible. Our professional teams treat all property damage with immense care.</p>
  </section>

  <aside class="panel" role="img" aria-label="Technician in protective suit and respirator holding a sprayer, tinted light blue"></aside>
  <h1 class="title title--right">Other Services<br>Offered By<br><span class="thin">Our Team</span><span class="rule"></span></h1>
  <p class="panel-intro">At <em>Brookvale Restoration</em>, we understand the impact of such a devastating incident. Our certified and experienced technicians possess compassion and respect for the situation and an unwavering attention to detail.</p>
  <ul class="extras">
    <li><svg width="27" height="25" viewBox="0 0 27 25" aria-hidden="true"><rect x="2" y="5" width="18" height="18" fill="none" stroke="var(--ink)" stroke-width="3"/><path d="M6 13 L11 18 L25 2" fill="none" stroke="var(--ink)" stroke-width="3.5"/></svg>Crime Scene And Trauma Cleanup</li>
    <li><svg width="27" height="25" viewBox="0 0 27 25" aria-hidden="true"><rect x="2" y="5" width="18" height="18" fill="none" stroke="var(--ink)" stroke-width="3"/><path d="M6 13 L11 18 L25 2" fill="none" stroke="var(--ink)" stroke-width="3.5"/></svg>Covid-19 Cleaning</li>
    <li><svg width="27" height="25" viewBox="0 0 27 25" aria-hidden="true"><rect x="2" y="5" width="18" height="18" fill="none" stroke="var(--ink)" stroke-width="3"/><path d="M6 13 L11 18 L25 2" fill="none" stroke="var(--ink)" stroke-width="3.5"/></svg>Carpet And Furniture Cleaning</li>
    <li><svg width="27" height="25" viewBox="0 0 27 25" aria-hidden="true"><rect x="2" y="5" width="18" height="18" fill="none" stroke="var(--ink)" stroke-width="3"/><path d="M6 13 L11 18 L25 2" fill="none" stroke="var(--ink)" stroke-width="3.5"/></svg>Junk Removal</li>
    <li><svg width="27" height="25" viewBox="0 0 27 25" aria-hidden="true"><rect x="2" y="5" width="18" height="18" fill="none" stroke="var(--ink)" stroke-width="3"/><path d="M6 13 L11 18 L25 2" fill="none" stroke="var(--ink)" stroke-width="3.5"/></svg>Asbestos Removal</li>
  </ul>

  <div class="foot-bar"></div>
</main>
</body>
</html>
```